Menu Design for Indian Restaurant

We are a new Indian restaurant, named Saffron Lantern Restaurant, looking for a sophisticated looking menu. It is a semi-formal dining restaurant with wooden tables and chairs and will have a focus on a creating a lively atmosphere. Environment-friendly products will be used, and the menu will be 100% vegetarian. There will be an emphasis on fresh, healthy and delicious food. We will be targeting vegans, vegetarians, health conscious people, people from all age groups, Indians, Australian's as well as other ethnic communities. We need a clean, simple, sophisticated design for the new restaurant menu. Attached is the restaurant logo for reference.

UPDATE:
- We have attached the menu
- We are not looking for any particular type of layout or size (open to suggests). Please suggest this after having a look at the menu contents. However, we will be having one formal menu to be used in the restaurant, and one in brochure form for distribution.
- There are no images at present. If you feel the need of images, please use sample images for now.

Thank you for the entries thus far.
Updates

Target Market(s)

All age groups from different nationalities

Industry/Entity Type

Indian Restaurant

Colors

Designer to choose colors to be used in the design.

Requirements
Nice to have
• This will be printed on environmentally friendly paper.

```html
<!DOCTYPE html>
<html lang="en">
<head>
<meta charset="utf-8">
<title>Saffron Lantern Restaurant – Menu</title>
<link rel="stylesheet" href="https://fonts.googleapis.com/css2?family=Playfair+Display:ital,wght@1,600;1,700&family=Roboto+Condensed:wght@400;700&display=swap">
<style>
:root{
  --green-deep:#0d3a22;
  --green-band:#2f7a3f;
  --green-text:#1f6b35;
  --gold:#f2cf4a;
  --cream:#f5f5ef;
  --ink:#2b2b2b;
  --muted:#d6e2d6;
}
*{box-sizing:border-box;margin:0;padding:0}
html,body{width:849px;height:1200px;overflow:hidden;background:#fff}
.menu{position:relative;width:849px;height:1200px;font-family:"Roboto Condensed",Arial,sans-serif;overflow:hidden}
.col-left{position:absolute;left:0;top:0;width:425px;height:1200px;background:linear-gradient(180deg,var(--green-deep),#0a2e1b)}
.col-right{position:absolute;left:425px;top:0;width:424px;height:1200px;background:var(--cream)}
.photo{position:absolute}
.photo-starter{left:0;top:0;width:425px;height:226px;background:radial-gradient(circle at 55% 55%,#c9a55a,#6b4a22 45%,#2a1a0e 80%)}
.photo-dessert{left:425px;top:0;width:424px;height:226px;background:linear-gradient(120deg,#e7c8cf,#d27f98 45%,#7a3b4f)}
.photo-banquet{left:30px;top:700px;width:190px;height:120px;background:linear-gradient(135deg,#8a6a3a,#3c2b16);border:2px solid var(--gold)}
.photo-tea{left:650px;top:600px;width:199px;height:280px;background:radial-gradient(circle at 50% 45%,#5a4032,#2a1d16 60%,#c8b89a 100%)}
.photo-platter{left:425px;top:1045px;width:424px;height:155px;background:linear-gradient(150deg,#e3d7b8,#8ea04a 40%,#c25b2a 75%,#4a2f1a)}
.band{position:absolute;font-family:"Playfair Display",Georgia,serif;font-style:italic;font-weight:700}
.band-left{left:0;width:425px;height:34px;background:var(--green-band);color:#fff;font-size:22px;line-height:34px;padding-left:50px}
.band-right{left:440px;color:var(--green-text);font-size:22px}
.items{position:absolute;list-style:none}
.left-items{left:30px;width:370px}
.left-items li{margin-bottom:6px}
.left-items .name{color:var(--gold);font-weight:700;font-size:12px;letter-spacing:.3px}
.left-items .desc{color:var(--muted);font-size:9.5px;line-height:1.25;white-space:nowrap}
.right-items{font-size:11px;color:var(--ink);letter-spacing:.3px}
.right-items li{margin-bottom:6px;white-space:nowrap}
.banquet-label{position:absolute;left:30px;top:744px;width:190px;text-align:center;color:#fff;font-weight:700;font-size:22px;letter-spacing:2px}
.banquet-info{position:absolute;left:230px;top:724px;width:180px;color:#fff;font-size:10px;text-align:center;line-height:1.35}
.banquet-info strong{display:block;color:var(--gold);font-size:12px;margin-bottom:4px}
</style>
</head>
<body>
<main class="menu">
  <section class="col-left"></section>
  <section class="col-right"></section>

  <div class="photo photo-starter" role="img" aria-label="Plate of crispy sev puri street snacks"></div>
  <div class="photo photo-dessert" role="img" aria-label="Glasses of pink layered dessert"></div>
  <div class="photo photo-tea" role="img" aria-label="Teapot and cups of masala tea"></div>
  <div class="photo photo-platter" role="img" aria-label="Platter of grilled vegetable skewers"></div>

  <h2 class="band band-left" style="top:248px">Gujrati Masti</h2>
  <ul class="items left-items" style="top:294px">
    <li><div class="name">SEV BATATA PURI (5) 8.9</div><div class="desc">Crisp puri topped with potato, sweet chutney and fine sev. Served with fresh coriander.</div></li>
    <li><div class="name">PANI PURI (6) 8.9</div><div class="desc">Hollow puri with spiced potato and tangy mint water.</div></li>
    <li><div class="name">DAHI BATATA PURI (6) 8.9</div><div class="desc">Puri filled with potato, chilled yoghurt and chutneys.</div></li>
    <li><div class="name">BHEL PURI 8.9</div><div class="desc">Puffed rice tossed with onion, tomato and tamarind chutney.</div></li>
    <li><div class="name">KOTHIMBIR VADI (4PCS) 8.9</div><div class="desc">Fried coriander and gram flour squares with green chutney.</div></li>
  </ul>

  <h2 class="band band-left" style="top:500px">Flavoured Indian Rice</h2>
  <ul class="items left-items" style="top:546px">
    <li><div class="name">CHITRANNA 8.9</div><div class="desc">Lemon rice tempered with peanuts, curry leaves and turmeric.</div></li>
    <li><div class="name">PULAO RICE 8.9</div><div class="desc">Fragrant basmati cooked with whole spices and peas.</div></li>
    <li><div class="name">STEAMED BASMATI 5.9</div><div class="desc">Long grain basmati rice, simply steamed.</div></li>
    <li><div class="name">VEGETABLE BIRYANI 13.9</div><div class="desc">Layered basmati with seasonal vegetables and saffron.</div></li>
  </ul>

  <div class="photo photo-banquet" role="img" aria-label="Banquet table of shared dishes"></div>
  <div class="banquet-label">BANQUET</div>
  <div class="banquet-info"><strong>BANQUET FOR 4 PEOPLE 24.9</strong>2 starters, 2 curries, rice, bread and dessert of your choice</div>

  <h2 class="band band-left" style="top:850px">Pizza</h2>
  <ul class="items left-items" style="top:896px">
    <li><div class="name">TROPICANA 11.9</div><div class="desc">Pineapple, capsicum, mozzarella and sweet chilli sauce.</div></li>
    <li><div class="name">MEXICANA 12.9</div><div class="desc">Jalapeño, capsicum, beans, onion and spicy salsa.</div></li>
    <li><div class="name">SICILIANA 12.9</div><div class="desc">Olives, sundried tomato, basil and fresh mozzarella.</div></li>
    <li><div class="name">KALAMATA 12.9</div><div class="desc">Kalamata olives, feta, spinach and red onion.</div></li>
    <li><div class="name">INDIANA 12.9</div><div class="desc">Tandoori paneer, capsicum, onion and mint drizzle.</div></li>
  </ul>

  <h2 class="band band-right" style="top:248px">Tawa &amp; Tandoori Breads</h2>
  <ul class="items right-items" style="left:460px;top:292px">
    <li>HOT PLATE CHAPATI 1.9</li><li>TANDOORI ROTI 2.9</li><li>NAAN 3.9</li><li>GARLIC NAAN 4.9</li><li>BUTTER NAAN 4.9</li>
  </ul>
  <ul class="items right-items" style="left:650px;top:292px">
    <li>ALOO KULCHA 4.9</li><li>PANEER KULCHA 5.9</li><li>KASHMIRI NAAN 5.9</li><li>MISSI ROTI 3.9</li><li>MAKKI DI ROTI 3.9</li>
  </ul>

  <h2 class="band band-right" style="top:412px">Dessert</h2>
  <ul class="items right-items" style="left:460px;top:454px">
    <li>GULAB JAMUN (2) 3.9</li><li>RASMALAI (2) 4.9</li><li>MANGO KULFI 4.9</li><li>PISTA KULFI 4.9</li>
  </ul>
  <ul class="items right-items" style="left:650px;top:454px">
    <li>GAJRELA (CARROT HALWA) 4.9</li><li>MOONG DAL HALWA 4.9</li><li>SABUDANA KHEER 4.9</li>
  </ul>

  <h2 class="band band-right" style="top:560px">Accompaniments</h2>
  <ul class="items right-items" style="left:460px;top:604px">
    <li>KACHUMBER SALAD 2.9</li><li>GREEN SALAD 4.9</li><li>ONION SALAD 2.9</li><li>RAITA CUCUMBER 3.9</li><li>RAITA CUCUMBER CARROTS 3.9</li><li>PICKLE 2.9</li><li>MANGO CHUTNEY 2.9</li><li>PAPPADAM SOUTH (2) 1.9</li><li>PAPPADAM BLACK PEPPER (2) 1.9</li>
  </ul>

  <h2 class="band band-right" style="top:900px">Beverages</h2>
  <ul class="items right-items" style="left:460px;top:944px">
    <li>MASALA TEA ........ 3.9</li><li>MASALA COFFEE ........ 3.9</li><li>HOT FRESH MILK WITH JALEBI (2 PIECES) 4.9</li><li>SERVED 3 TO 6:30 PM</li>
  </ul>
</main>
</body>
</html>
```